Bref créative
Brightfield Signal STATIONARY
business cards and letterhead
Professional
Alan Vortmeyer
President
4172 Tamsin Street
Larkmoor, Westvale
L3P 7R2
alan@brightfieldsignal.ca
brightfieldsignal.ca

```html
<!DOCTYPE html>
<html lang="en">
<head>
<meta charset="utf-8">
<title>Brightfield Signal — Stationery</title>
<link href="https://fonts.googleapis.com/css2?family=Open+Sans:wght@400;600;700&display=swap" rel="stylesheet">
<style>
  :root {
    --backdrop: #eceef1;
    --paper: #ffffff;
    --brand-blue: #1e9be9;
    --brand-blue-light: #5cc0f7;
    --swoosh-grey: #6b6f75;
    --ink: #3c4046;
    --ink-soft: #7d838b;
  }
  * { box-sizing: border-box; margin: 0; padding: 0; }
  html, body { width: 1200px; height: 936px; overflow: hidden; }
  body { background: var(--backdrop); font-family: "Open Sans", Arial, sans-serif; color: var(--ink); }
  .canvas { position: relative; width: 1200px; height: 936px; overflow: hidden; }

  .sheet { position: absolute; background: var(--paper); overflow: hidden; }
  .wave { position: absolute; left: 0; bottom: 0; width: 100%; display: block; }
  .web-line {
    position: absolute; left: 0; right: 0; text-align: center;
    color: #fff; font-weight: 600; letter-spacing: 0.28em;
  }

  .brand { position: absolute; display: flex; align-items: center; }
  .brand-dot { border-radius: 50%; background: var(--brand-blue); flex: none; }
  .brand-name { font-weight: 700; color: var(--brand-blue); text-transform: uppercase; white-space: nowrap; letter-spacing: 0.01em; }

  /* Letterhead */
  .letterhead { left: 127px; top: 63px; width: 412px; height: 557px; }
  .letterhead .brand { left: 26px; top: 28px; gap: 7px; }
  .letterhead .brand-dot { width: 26px; height: 26px; }
  .letterhead .brand-name { font-size: 11px; }
  .contact-list { position: absolute; left: 252px; top: 20px; list-style: none; font-size: 6.5px; line-height: 11px; color: var(--ink-soft); }
  .contact-list li { display: flex; align-items: center; gap: 5px; }
  .contact-list .icon { width: 7px; height: 7px; border-radius: 50%; background: var(--brand-blue); flex: none; }
  .letterhead .web-line { bottom: 14px; font-size: 8px; }

  /* Presentation folder */
  .folder { left: 633px; top: 43px; width: 493px; height: 620px; }
  .folder .brand { left: 60px; top: 250px; gap: 14px; }
  .folder .brand-dot { width: 74px; height: 74px; }
  .folder .brand-name { font-size: 29px; }
  .folder .web-line { bottom: 16px; font-size: 9px; }

  /* Business cards */
  .card { left: 43px; width: 192px; height: 107px; }
  .card-front { top: 653px; }
  .card-back { top: 779px; }
  .card .brand { left: 10px; top: 10px; gap: 5px; }
  .card .brand-dot { width: 16px; height: 16px; }
  .card .brand-name { font-size: 8px; }
  .card-details { position: absolute; left: 98px; top: 30px; font-size: 5px; line-height: 7px; color: var(--ink-soft); }
  .card-details .person { font-weight: 700; color: var(--ink); font-size: 6px; }
  .card-back .brand { top: 36px; }
  .card-back .brand-dot { width: 24px; height: 24px; }
  .card .web-line { bottom: 4px; font-size: 5px; }

  /* Envelope front */
  .envelope-front { left: 266px; top: 653px; width: 341px; height: 220px; }
  .envelope-front .brand { left: 18px; top: 18px; gap: 6px; }
  .envelope-front .brand-dot { width: 22px; height: 22px; }
  .envelope-front .brand-name { font-size: 10px; }
  .return-address { position: absolute; left: 46px; top: 46px; font-size: 5.5px; color: var(--ink-soft); }
  .envelope-front .web-line { bottom: 10px; font-size: 7px; }

  /* Envelope back */
  .envelope-back { left: 734px; top: 670px; width: 430px; height: 203px; }
  .flap { position: absolute; left: 0; top: 0; width: 100%; height: 90px; display: block; }
  .envelope-back .web-line { top: 24px; font-size: 8px; }
</style>
</head>
<body>
<main class="canvas">

  <section class="sheet letterhead" aria-label="Letterhead">
    <div class="brand"><span class="brand-dot"></span><span class="brand-name">Brightfield Signal</span></div>
    <ul class="contact-list">
      <li><span class="icon"></span>4172 Tamsin Street Larkmoor,<br>Westvale L3P 7R2</li>
      <li><span class="icon"></span>(905) 555-0148</li>
      <li><span class="icon"></span>alan@brightfieldsignal.ca</li>
      <li><span class="icon"></span>www.brightfieldsignal.ca</li>
    </ul>
    <svg class="wave" viewBox="0 0 400 110" height="110" preserveAspectRatio="none" aria-hidden="true">
      <path d="M0 42 C120 78 270 8 400 34 L400 110 L0 110Z" fill="var(--brand-blue-light)"/>
      <path d="M0 52 C130 86 270 22 400 44 L400 110 L0 110Z" fill="var(--brand-blue)"/>
      <path d="M0 30 C120 62 250 2 400 20" fill="none" stroke="var(--swoosh-grey)" stroke-width="3"/>
    </svg>
    <p class="web-line">www.brightfieldsignal.ca</p>
  </section>

  <section class="sheet folder" aria-label="Presentation folder">
    <div class="brand"><span class="brand-dot"></span><span class="brand-name">Brightfield Signal</span></div>
    <svg class="wave" viewBox="0 0 400 110" height="110" preserveAspectRatio="none" aria-hidden="true">
      <path d="M0 42 C120 78 270 8 400 34 L400 110 L0 110Z" fill="var(--brand-blue-light)"/>
      <path d="M0 52 C130 86 270 22 400 44 L400 110 L0 110Z" fill="var(--brand-blue)"/>
      <path d="M0 30 C120 62 250 2 400 20" fill="none" stroke="var(--swoosh-grey)" stroke-width="3"/>
    </svg>
    <p class="web-line">www.brightfieldsignal.ca</p>
  </section>

  <section class="sheet card card-front" aria-label="Business card front">
    <div class="brand"><span class="brand-dot"></span><span class="brand-name">Brightfield Signal</span></div>
    <div class="card-details">
      <p class="person">Alan Vortmeyer</p>
      <p>President</p>
      <p>4172 Tamsin Street</p>
      <p>Larkmoor, Westvale L3P 7R2</p>
      <p>alan@brightfieldsignal.ca</p>
    </div>
    <svg class="wave" viewBox="0 0 400 110" height="24" preserveAspectRatio="none" aria-hidden="true">
      <path d="M0 42 C120 78 270 8 400 34 L400 110 L0 110Z" fill="var(--brand-blue)"/>
      <path d="M0 30 C120 62 250 2 400 20" fill="none" stroke="var(--swoosh-grey)" stroke-width="5"/>
    </svg>
  </section>

  <section class="sheet card card-back" aria-label="Business card back">
    <div class="brand"><span class="brand-dot"></span><span class="brand-name">Brightfield Signal</span></div>
    <svg class="wave" viewBox="0 0 400 110" height="20" preserveAspectRatio="none" aria-hidden="true">
      <path d="M0 42 C120 78 270 8 400 34 L400 110 L0 110Z" fill="var(--brand-blue)"/>
    </svg>
    <p class="web-line">www.brightfieldsignal.ca</p>
  </section>

  <section class="sheet envelope-front" aria-label="Envelope front">
    <div class="brand"><span class="brand-dot"></span><span class="brand-name">Brightfield Signal</span></div>
    <p class="return-address">4172 Tamsin Street Larkmoor, Westvale L3P 7R2</p>
    <svg class="wave" viewBox="0 0 400 110" height="56" preserveAspectRatio="none" aria-hidden="true">
      <path d="M0 42 C120 78 270 8 400 34 L400 110 L0 110Z" fill="var(--brand-blue-light)"/>
      <path d="M0 52 C130 86 270 22 400 44 L400 110 L0 110Z" fill="var(--brand-blue)"/>
      <path d="M0 30 C120 62 250 2 400 20" fill="none" stroke="var(--swoosh-grey)" stroke-width="3"/>
    </svg>
    <p class="web-line">www.brightfieldsignal.ca</p>
  </section>

  <section class="sheet envelope-back" aria-label="Envelope back">
    <svg class="flap" viewBox="0 0 430 90" preserveAspectRatio="none" aria-hidden="true">
      <path d="M0 0 H430 V56 C320 86 130 50 0 74Z" fill="var(--brand-blue)"/>
      <path d="M0 74 C130 50 320 86 430 56" fill="none" stroke="var(--brand-blue-light)" stroke-width="2"/>
    </svg>
    <p class="web-line">www.brightfieldsignal.ca</p>
  </section>

</main>
</body>
</html>
```